Business Stationery Design

I would like to get some stationery designed for my company. The stationery should include a letterhead, envelope, and business card. We are a technology consulting company specializing in Healthcare IT, and Education management systems. The colors of the stationery should match the logo. The logo is uploaded.

Target Market(s)

Hospitals, Clinics. Doctors offices. Private Schools.

Industry/Entity Type

Business

```html
<!DOCTYPE html>
<html lang="en">
<head>
<meta charset="utf-8">
<title>Clearfield Partners – Business Card</title>
<link href="https://fonts.googleapis.com/css2?family=Roboto:wght@400;500&display=swap" rel="stylesheet">
<style>
  :root{
    --backdrop:#d8d5cf;
    --card-frost:#ebe9e4;
    --orange-light:#f6b43a;
    --orange-deep:#e88a14;
    --green:#3d9b2c;
    --ink:#5a5750;
    --text-light:#fff6e6;
    --divider:rgba(255,246,230,.6);
  }
  html,body{margin:0;padding:0;width:1200px;height:969px;overflow:hidden;background:var(--backdrop);}
  .canvas{position:relative;width:1200px;height:969px;}
  .card{position:absolute;left:100px;top:200px;width:1000px;height:569px;background:var(--card-frost);
    box-shadow:0 10px 30px rgba(0,0,0,.18);overflow:hidden;font-family:'Roboto',sans-serif;}
  .card-shapes{position:absolute;inset:0;width:100%;height:100%;}
  .wordmark{position:absolute;left:640px;top:110px;display:flex;align-items:center;gap:14px;}
  .wordmark-square{width:22px;height:22px;background:var(--ink);}
  .wordmark-name{font-size:34px;font-weight:400;line-height:1;color:var(--ink);}
  .person{position:absolute;left:52px;top:300px;color:var(--text-light);}
  .person-name{font-size:30px;font-weight:500;letter-spacing:.5px;}
  .person-title{font-size:21px;margin-top:6px;}
  .contacts{position:absolute;left:52px;top:398px;color:var(--text-light);font-size:20px;list-style:none;margin:0;padding:0;}
  .contacts li{display:flex;align-items:center;height:33px;}
  .contacts svg{width:20px;height:20px;margin-right:14px;fill:var(--text-light);}
  .divider{position:absolute;left:340px;top:395px;width:1px;height:125px;background:var(--divider);}
  .address{position:absolute;left:370px;top:415px;color:var(--text-light);font-size:20px;line-height:32px;}
  .web{letter-spacing:4px;}
</style>
</head>
<body>
<div class="canvas">
  <div class="card">
    <svg class="card-shapes" viewBox="0 0 580 330" preserveAspectRatio="none" aria-hidden="true">
      <defs>
        <linearGradient id="orangeBand" x1="0" y1="0" x2="1" y2="1">
          <stop offset="0" stop-color="var(--orange-light)"/>
          <stop offset="1" stop-color="var(--orange-deep)"/>
        </linearGradient>
      </defs>
      <path d="M0,80 C20,100 60,110 100,118 C250,150 450,190 580,262 L580,330 L0,330 Z" fill="url(#orangeBand)"/>
      <path d="M30,112 C200,145 420,195 580,272" fill="none" stroke="var(--green)" stroke-width="3"/>
      <path d="M60,118 C230,150 440,205 580,285" fill="none" stroke="var(--green)" stroke-width="2.5"/>
    </svg>

    <div class="wordmark">
      <span class="wordmark-square"></span>
      <span class="wordmark-name">Clearfield Partners</span>
    </div>

    <div class="person">
      <div class="person-name">DANIEL REYES</div>
      <div class="person-title">CEO/FOUNDER</div>
    </div>

    <ul class="contacts">
      <li><svg viewBox="0 0 24 24"><path d="M6.6 10.8a15 15 0 0 0 6.6 6.6l2.2-2.2c.3-.3.7-.4 1-.2 1.1.4 2.3.6 3.6.6.6 0 1 .4 1 1V20c0 .6-.4 1-1 1A17 17 0 0 1 3 4c0-.6.4-1 1-1h3.5c.6 0 1 .4 1 1 0 1.3.2 2.5.6 3.6.1.3 0 .7-.2 1z"/></svg>555 214 7730</li>
      <li><svg viewBox="0 0 24 24"><path d="M7 1h10a2 2 0 0 1 2 2v18a2 2 0 0 1-2 2H7a2 2 0 0 1-2-2V3a2 2 0 0 1 2-2zm0 3v14h10V4zm5 15.5a1 1 0 1 0 0 2 1 1 0 0 0 0-2z"/></svg>555 318 4426</li>
      <li><svg viewBox="0 0 24 24"><path d="M6 2h10v5H6zM3 8h18a1 1 0 0 1 1 1v9a1 1 0 0 1-1 1h-3v3H6v-3H3a1 1 0 0 1-1-1V9a1 1 0 0 1 1-1zm5 8v4h8v-4z"/></svg>555 902 6158</li>
      <li><svg viewBox="0 0 24 24"><path d="M2 5h20v14H2zm2 2v.5l8 5 8-5V7zm0 2.8V17h16V9.8l-8 5z"/></svg>daniel@clearfield.com</li>
    </ul>

    <div class="divider"></div>

    <div class="address">
      <div>2140 Willow Creek Road</div>
      <div>Fairview, Oregon 97024</div>
      <div class="web">www.clearfield.com</div>
    </div>
  </div>
</div>
</body>
</html>
```